Business card design for global fintech startup

Veltrix is a modern payments platform for the global insurance industry, serving international health, life, and travel insurers, MGAs, brokers, and partners.

We need a professional, premium business card for use at insurance conferences and executive meetings. The goal is to create a card that feels trustworthy, modern, and high-quality, while still being distinctive and memorable in a stack of business cards.

Target audience:
Senior insurance executives (VP, C-suite).

Design goals:
Clear, professional, and credible
Modern but not trendy
Premium and well-structured
Easy to read and practical for networking

Brand direction:
Brand-first (company over individual)
Follow existing brand guidelines where possible
Clean layout, strong hierarchy, excellent readability

Must include:
Name
Title
Company name (Veltrix)
Logo
Email
Phone/Whatsapp
Website (www.withveltrix.example)
Tagline - Payments Built On Trust

Materials & finish:
Open to designer recommendations for premium look and feel.

Please avoid:
Flashy or trendy startup styles
Generic insurance icons or clichés
Cluttered layouts or hard-to-read text

Deliverables:
Front and back business card, print-ready files.

Target Market(s)

Global Insurance executives

Industry/Entity Type

Fintech, Insurtech, Insurance, Financial Services

Contact Information for Business Card

Name Title Company name (Veltrix) Logo Email Phone/Whatsapp Website (www.withveltrix.example) Tagline - Payments Built On Trust

Font styles to use
Other font styles liked:
• See brand guidelines

Requirements
Nice to have
• something that stands out/makes us more memorable while still remaining professional
Should not have
• Please avoid: Flashy or trendy startup styles Generic insurance icons or clichés Cluttered layouts or hard-to-read text

```html
<!DOCTYPE html>
<html lang="en">
<head>
<meta charset="utf-8">
<title>Veltrix business cards</title>
<link rel="stylesheet" href="https://fonts.googleapis.com/css2?family=Ubuntu:wght@400;500&family=Roboto:wght@400;500&display=swap">
<style>
  :root {
    --page: #ebe8e4;
    --ink: #1d1d1f;
    --white: #ffffff;
    --black: #000000;
    --red: #c8202f;
    --purple: #5b3f9e;
    --orange: #f07f22;
    --sky: #a7e3f3;
    --cream: #fbf0e6;
    --rule: #8a8a8a;
    --shadow: 0 6px 18px rgba(0,0,0,.18);
  }
  * { margin: 0; padding: 0; box-sizing: border-box; }
  html, body { width: 1200px; height: 995px; overflow: hidden; background: var(--page); }
  .sheet {
    position: relative; width: 1200px; height: 995px;
    display: grid; grid-template-columns: 540px 540px; grid-template-rows: 310px 310px;
    gap: 60px 40px; padding: 157px 40px;
  }
  .card { position: relative; overflow: hidden; box-shadow: var(--shadow); font-family: "Ubuntu", sans-serif; color: var(--ink); }
  .card--white { background: var(--white); }
  .card--black { background: var(--black); color: var(--white); }
  .card--gradient { background: linear-gradient(120deg, var(--sky) 0%, #c9ecf2 45%, var(--cream) 80%, var(--white) 100%); }

  /* brand name mark */
  .brand { position: absolute; display: flex; align-items: center; gap: 14px; font-weight: 500; }
  .brand__dot { border-radius: 50%; background: var(--orange); flex: none; }

  /* front */
  .front .brand { left: 70px; top: 44px; font-size: 58px; letter-spacing: 8px; text-transform: uppercase; }
  .front .brand__dot { width: 40px; height: 40px; }
  .person { position: absolute; right: 318px; top: 170px; text-align: right; font-family: "Roboto", sans-serif; }
  .person__name { color: var(--red); font-weight: 500; font-size: 20px; letter-spacing: .5px; }
  .person__title { font-size: 14px; margin-top: 2px; }
  .divider { position: absolute; left: 238px; top: 150px; width: 2px; height: 100px; background: linear-gradient(var(--white), var(--rule), var(--white)); }
  .contacts { position: absolute; left: 260px; top: 150px; list-style: none; font-family: "Roboto", sans-serif; font-size: 14px; }
  .contacts li { display: flex; align-items: center; gap: 8px; height: 25px; }
  .contacts svg { width: 15px; height: 15px; flex: none; }
  .front .tagline-small { position: absolute; left: 40px; bottom: 30px; font-family: "Roboto", sans-serif; font-size: 14px; letter-spacing: .6px; }

  /* backs */
  .tagline { font-weight: 500; line-height: 1.1; }
  .url { font-size: 18px; letter-spacing: 2.5px; margin-top: 14px; white-space: nowrap; }
  .url__name { color: var(--purple); }
  .card--black .url__name { color: var(--white); }

  .back-wide .brand { left: 50%; top: 56px; transform: translateX(-50%); font-size: 30px; }
  .back-wide .brand__dot { width: 22px; height: 22px; }
  .back-wide .copy { position: absolute; left: 0; right: 0; top: 130px; text-align: center; }
  .back-wide .tagline { font-size: 42px; }

  .back-split .brand { left: 40px; top: 120px; font-size: 46px; }
  .back-split .brand__dot { width: 34px; height: 34px; }
  .back-split .copy { position: absolute; left: 280px; top: 98px; width: 230px; }
  .back-split .tagline { font-size: 30px; }
  .back-split .rule { height: 1px; width: 210px; background: var(--rule); margin-top: 12px; }
  .back-split .url { font-size: 14px; letter-spacing: 1.2px; }
</style>
</head>
<body>
<main class="sheet">

  <section class="card card--white front" aria-label="Card front">
    <div class="brand"><span class="brand__dot"></span>Veltrix</div>
    <div class="person">
      <p class="person__name">DANIEL MOREAU</p>
      <p class="person__title">Owner</p>
    </div>
    <div class="divider"></div>
    <ul class="contacts">
      <li><svg viewBox="0 0 16 16"><circle cx="8" cy="8" r="7" fill="none" stroke="#1d1d1f" stroke-width="1.4"/><path d="M6 4.5l1.2 2-1 1c.6 1.3 1.2 1.9 2.4 2.4l1-1 2 1.2-.8 1.6c-3 0-6-3-6-6z" fill="#1d1d1f"/></svg>555.010.1234</li>
      <li><svg viewBox="0 0 16 16"><rect x="4.5" y="1" width="7" height="14" rx="1.5" fill="none" stroke="#1d1d1f" stroke-width="1.4"/><circle cx="8" cy="12.5" r=".9" fill="#1d1d1f"/></svg>555.010.7890</li>
      <li><svg viewBox="0 0 16 16"><rect x="1.5" y="3.5" width="13" height="9" fill="none" stroke="#1d1d1f" stroke-width="1.4"/><path d="M1.5 3.5l6.5 5 6.5-5" fill="none" stroke="#1d1d1f" stroke-width="1.4"/></svg>info@withveltrix.example</li>
      <li><svg viewBox="0 0 16 16"><g fill="none" stroke="#1d1d1f" stroke-width="1.2"><circle cx="8" cy="8" r="6.5"/><ellipse cx="8" cy="8" rx="3" ry="6.5"/><path d="M1.5 8h13M2.5 4.8h11M2.5 11.2h11"/></g></svg>www.withveltrix.example</li>
    </ul>
    <p class="tagline-small">PAYMENTS BUILT ON TRUST</p>
  </section>

  <section class="card card--gradient back-wide" aria-label="Card back, tagline">
    <div class="brand"><span class="brand__dot"></span>Veltrix</div>
    <div class="copy">
      <p class="tagline">Payments Built On Trust</p>
      <p class="url">www.<span class="url__name">withveltrix</span>.example</p>
    </div>
  </section>

  <section class="card card--black back-split" aria-label="Card back, dark">
    <div class="brand"><span class="brand__dot"></span>Veltrix</div>
    <div class="copy">
      <p class="tagline">Payments Built<br>On Trust</p>
      <div class="rule"></div>
      <p class="url">www.<span class="url__name">withveltrix</span>.example</p>
    </div>
  </section>

  <section class="card card--gradient back-split" aria-label="Card back, light">
    <div class="brand"><span class="brand__dot"></span>Veltrix</div>
    <div class="copy">
      <p class="tagline">Payments Built<br>On Trust</p>
      <div class="rule"></div>
      <p class="url">www.<span class="url__name">withveltrix</span>.example</p>
    </div>
  </section>

</main>
</body>
</html>
```